Sports Performance Lab needs a new website

We need an updated/new website for Vondel Arc Human Performance Lab. We recently moved from Florida to the Chicago area. We perform testing ranging from VO2 Max, Lactate Threshold, Resting Metabolic Rate, Body Composition Testing with the TRU SHELL and Metabolic Efficiency Testing. We also have a mobile lab contained in a 24 foot trailer. We work with athletes, coaches, Fitness Gyms, Pivot Drill Gyms to improve performance and also with people looking to manage or lose weight. Our current site is www.vondelarclab.example. Looking for an improved site, better grahics/photos but also blends into our current logo and graphics on Mobile Lab. Would like a calendar/ appointment page on website

Colors
ec1f27
000000
fbed22

Requirements
Must have
• ability to easily updatae
Nice to have
• appointment calendar

```html
<!DOCTYPE html>
<html lang="en">
<head>
<meta charset="utf-8">
<title>Vondel Arc Human Performance Lab</title>
<link href="https://fonts.googleapis.com/css2?family=Raleway:wght@400;500;600;700;800&display=swap" rel="stylesheet">
<style>
:root{
  --red:#ec1f27;
  --red-dark:#c4151b;
  --yellow:#fbed22;
  --black:#000000;
  --ink:#2b2b2b;
  --grey:#555555;
  --white:#ffffff;
  --line:#dddddd;
}
*{box-sizing:border-box;margin:0;padding:0}
html,body{width:1200px;height:2400px;overflow:hidden}
body{position:relative;background:var(--white);font-family:"Raleway",sans-serif;color:var(--ink)}
.abs{position:absolute}

/* header */
.site-header{left:0;top:0;width:1200px;height:96px;background:var(--white)}
.brand{left:75px;top:22px}
.brand-name{font-size:24px;font-weight:800;color:var(--black);letter-spacing:.5px;line-height:28px;display:flex;align-items:center;gap:7px}
.brand-name .mark{width:12px;height:12px;background:var(--red)}
.brand-tag{font-size:9px;font-weight:700;color:var(--black);letter-spacing:1.2px;text-transform:uppercase;margin-top:3px;padding-top:3px;border-top:3px solid var(--yellow)}
.connect{left:706px;top:24px}
.label{font-size:12px;font-weight:700;color:var(--black);text-transform:uppercase}
.socials{display:flex;gap:4px;margin-top:6px}
.socials span{width:31px;height:31px;border-radius:50%;background:#555}
.call{left:971px;top:24px}
.phone{font-size:24px;font-weight:700;color:var(--red);margin-top:4px}

/* nav */
.main-nav{left:0;top:96px;width:1200px;height:51px;background:linear-gradient(var(--red),var(--red-dark));display:flex;padding-left:75px}
.main-nav a{display:block;height:51px;line-height:51px;padding:0 20px;font-size:14px;font-weight:600;color:var(--white);text-decoration:none;text-transform:uppercase}
.main-nav a.active{background:var(--yellow);color:var(--red)}

/* hero */
.hero{left:0;top:147px;width:1200px;height:509px;background:linear-gradient(180deg,#6f9ec4 0%,#a9c7df 45%,#c9d9e6 75%,#8aa3b8 100%)}
.hero-arrow{top:233px}

/* welcome */
.section-title{font-size:23px;font-weight:700;text-transform:uppercase;letter-spacing:.5px}
.copy{font-size:13.5px;line-height:24px}
.welcome{left:75px;top:696px;width:770px}
.welcome .copy{color:var(--grey);margin-top:18px}
.welcome .copy + .copy{margin-top:10px}
.btn{display:block;width:165px;height:48px;line-height:48px;text-align:center;background:linear-gradient(var(--red),var(--red-dark));color:var(--white);font-size:14px;font-weight:700;text-transform:uppercase;border-radius:2px}

/* appointment */
.appointment{left:885px;top:619px;width:240px;height:448px;background:var(--yellow);border:3px solid var(--red)}
.appointment-head{height:45px;background:var(--black);color:var(--white);font-size:19px;font-weight:700;text-align:center;line-height:45px;text-transform:uppercase}
.field{position:absolute;left:16px;width:202px;height:32px;background:var(--white);border:1px solid #d6d6d6;font-size:12px;color:#777;padding:0 11px;line-height:30px}
.field svg{position:absolute;right:10px;top:10px}
.field.message{height:96px;line-height:20px;padding-top:6px}
.submit{position:absolute;left:35px;top:376px;width:165px;height:48px}

/* who */
.who{left:0;top:1035px;width:1200px;height:423px;background:var(--red)}
.who-text{left:75px;top:62px;width:600px}
.who-text .section-title{color:var(--yellow)}
.who-text .copy{color:var(--white);margin-top:20px}
.who .btn{position:absolute;left:75px;top:320px}
.who-photo{left:704px;top:69px;width:421px;height:298px;border:3px solid #9b0f14;background:linear-gradient(135deg,#2e2e2e,#5a5a5a 60%,#9a9a9a)}

/* testing */
.testing{left:0;top:1458px;width:1200px;height:398px}
.testing-yellow{left:0;top:0;width:405px;height:398px;background:var(--yellow)}
.testing-photo{left:405px;top:0;width:400px;height:398px;background:linear-gradient(160deg,#c88a3c,#8b5a2b 50%,#d9b98f)}
.testing-dark{left:0;top:0}
.services{left:75px;top:52px;width:320px}
.services .section-title{color:var(--black)}
.checklist{list-style:none;margin-top:16px}
.checklist li{position:relative;padding-left:28px;font-size:13.5px;line-height:21px;color:var(--black);margin-bottom:9px}
.checklist svg{position:absolute;left:0;top:3px}
.services .btn{margin-top:18px}
.needs{left:781px;top:42px;width:360px}
.needs .section-title{color:var(--yellow);line-height:28px}
.needs .copy{color:var(--white);margin-top:18px}
.needs .btn{margin-top:32px}

/* giving back */
.giving{left:75px;top:1930px;width:610px}
.giving .copy{color:var(--grey);margin-top:18px}
.giving .btn{margin-top:24px}
.giving-photo{left:704px;top:1899px;width:421px;height:296px;background:linear-gradient(140deg,#c6843a,#9a6a35 45%,#e0c7a3)}

/* footer */
.site-footer{left:0;top:2237px;width:1200px;height:163px;background:var(--black)}
.footer-nav{position:absolute;left:0;top:57px;width:1200px;text-align:center;font-size:13px;color:var(--white);text-transform:uppercase;letter-spacing:.3px}
.footer-nav span{margin:0 8px}
.copyright{position:absolute;left:0;top:90px;width:1200px;text-align:center;font-size:12.5px;color:#aaaaaa}
</style>
</head>
<body>

<header class="site-header abs">
  <div class="brand abs">
    <div class="brand-name"><span class="mark"></span>VONDEL ARC</div>
    <div class="brand-tag">Human Performance Lab</div>
  </div>
  <div class="connect abs">
    <div class="label">Connect Us</div>
    <div class="socials"><span></span><span></span><span></span><span></span><span></span><span></span></div>
  </div>
  <div class="call abs">
    <div class="label">Call Us Today</div>
    <div class="phone">312-555-0148</div>
  </div>
</header>

<nav class="main-nav abs">
  <a class="active">Home</a>
  <a>About Us</a>
  <a>Fitness Tests</a>
  <a>TRU SHELL</a>
  <a>Coaches Corner</a>
  <a>Corporate Wellness</a>
  <a>Contact</a>
</nav>

<div class="hero abs" role="img" aria-label="Smiling athlete in a plank position with overlaid heart-rate data graphics">
  <svg class="hero-arrow abs" style="left:60px" width="24" height="40" viewBox="0 0 24 40"><polyline points="20,2 4,20 20,38" fill="none" stroke="#fbed22" stroke-width="3"/></svg>
  <svg class="hero-arrow abs" style="left:1116px" width="24" height="40" viewBox="0 0 24 40"><polyline points="4,2 20,20 4,38" fill="none" stroke="#fbed22" stroke-width="3"/></svg>
</div>

<section class="welcome abs">
  <h2 class="section-title">Welcome to our website</h2>
  <p class="copy">Welcome to VONDEL ARC - your source for mobile human performance testing including V02Max, Lactic Threshold, Metabolic Rate, Metabolic Efficiency, and Body Composition.</p>
  <p class="copy">We use state of the art equipment by Meridia including the Gold Standard TRU SHELL in our completely self-contained mobile unit. Vondel Arc conducts both running and cycling assessments to ensure sport specific measurements to help you reach your peak performance goals. We also conduct body composition testing important for Pivot Drill athletes and those participating in fitness competition, as well as critical in weight management programs.</p>
  <a class="btn" style="margin-top:28px">Read More</a>
</section>

<section class="who abs">
  <div class="who-text abs">
    <h2 class="section-title">Who are we?</h2>
    <p class="copy">Vondel Arc is a mobile Sports and Human Performance Testing Center owned and operated by Rowan Kessler. Vondel Arc conducts both running and cycling assessments to ensure sports specific measurements to help reach your performance goals. Rowan is a National Tri Federation and Open Road Runners League Certified Coach and has been conducting fitness assessments for the past 5 years for his personal clients. NOW he is bringing this state of the art equipment directly to you for use with your coach, trainer, or clients! Not sure what to do with performance testing results...</p>
  </div>
  <a class="btn">Read More</a>
  <div class="who-photo abs" role="img" aria-label="Coach standing beside the egg-shaped body composition chamber with a client seated inside"></div>
</section>

<section class="testing abs">
  <div class="testing-yellow abs"></div>
  <div class="testing-photo abs" role="img" aria-label="Cyclist on a stationary bike wearing a metabolic test mask beside the analyser"></div>
  <svg class="testing-dark abs" width="1200" height="398" viewBox="0 0 1200 398"><polygon points="760,0 1200,0 1200,398 680,398" fill="#000000"/></svg>
  <div class="services abs">
    <h2 class="section-title">Testing Services</h2>
    <ul class="checklist">
      <li><svg width="16" height="16" viewBox="0 0 16 16"><circle cx="8" cy="8" r="8" fill="#000"/><polyline points="4.5,8.2 7,10.5 11.5,5.5" fill="none" stroke="#fbed22" stroke-width="2"/></svg>Body Composition Tracking with the TRU SHELL including Fat % - Lean % Analysis</li>
      <li><svg width="16" height="16" viewBox="0 0 16 16"><circle cx="8" cy="8" r="8" fill="#000"/><polyline points="4.5,8.2 7,10.5 11.5,5.5" fill="none" stroke="#fbed22" stroke-width="2"/></svg>Resting Metabolic Rate (RMR)</li>
      <li><svg width="16" height="16" viewBox="0 0 16 16"><circle cx="8" cy="8" r="8" fill="#000"/><polyline points="4.5,8.2 7,10.5 11.5,5.5" fill="none" stroke="#fbed22" stroke-width="2"/></svg>VO2 Max</li>
      <li><svg width="16" height="16" viewBox="0 0 16 16"><circle cx="8" cy="8" r="8" fill="#000"/><polyline points="4.5,8.2 7,10.5 11.5,5.5" fill="none" stroke="#fbed22" stroke-width="2"/></svg>Lactate Threshold</li>
      <li><svg width="16" height="16" viewBox="0 0 16 16"><circle cx="8" cy="8" r="8" fill="#000"/><polyline points="4.5,8.2 7,10.5 11.5,5.5" fill="none" stroke="#fbed22" stroke-width="2"/></svg>Calories per Hour - Metabolic Efficiency</li>
      <li><svg width="16" height="16" viewBox="0 0 16 16"><circle cx="8" cy="8" r="8" fill="#000"/><polyline points="4.5,8.2 7,10.5 11.5,5.5" fill="none" stroke="#fbed22" stroke-width="2"/></svg>Video Analysis with Stride Lens</li>
    </ul>
    <a class="btn">Read More</a>
  </div>
  <div class="needs abs">
    <h2 class="section-title">Who needs performance testing services</h2>
    <p class="copy">Vondel Arc mobile Sports and Human Performance Testing Center services are for all levels of athletes and sports from triathlon to Pivot Drill. The tests are specifically designed to help you understand your current level of fitness and provide you with data critical in developing your training plan.</p>
    <a class="btn">Read More</a>
  </div>
</section>

<section class="giving abs">
  <h2 class="section-title">Giving Back</h2>
  <p class="copy">Vondel Arc testing event for Strong Forward Vets Athletes at Gearhouse Cycles in Lakeport. We had the opportunity to provide free VO2Max and TRU SHELL testing for these amazing athletes who work to be at the top of their training and racing game! Thanks to Gearhouse Cycles for letting us use their facilities to conduct the tests for these athletes,<br>what a great partnership!</p>
  <a class="btn">Read More</a>
</section>
<div class="giving-photo abs" role="img" aria-label="Testing room with bikes on trainers and athletes resting on the floor after a session"></div>

<div class="appointment abs">
  <div class="appointment-head">Get Appointment</div>
  <div class="field" style="top:69px">Name</div>
  <div class="field" style="top:109px">Phone No</div>
  <div class="field" style="top:151px">Email Address</div>
  <div class="field" style="top:191px">Select Service<svg width="10" height="10" viewBox="0 0 10 10"><polyline points="2,3 5,6.5 8,3" fill="none" stroke="#777" stroke-width="1.5"/></svg></div>
  <div class="field" style="top:232px">Select Date<svg width="12" height="12" viewBox="0 0 12 12"><rect x="1" y="2" width="10" height="9" fill="none" stroke="#777" stroke-width="1.2"/><line x1="1" y1="5" x2="11" y2="5" stroke="#777" stroke-width="1.2"/></svg></div>
  <div class="field message" style="top:274px">Message</div>
  <a class="btn submit">Submit</a>
</div>

<footer class="site-footer abs">
  <div class="footer-nav">Home<span>/</span>About Us<span>/</span>Fitness Tests<span>/</span>TRU SHELL<span>/</span>Coaches Corner<span>/</span>Corporate Wellness<span>/</span>Contact</div>
  <div class="copyright">Copyright © 2016 Vondel Arc. All Right Reserved</div>
</footer>

</body>
</html>
```